Medical Clinic Website - New Private Clinic

We have a basic design for a website. Would like it developed in WORDPRESS. the attached JPG shows the page basic design.

Colours and overall design to be similar

MUST BE WORD PRESS and must allow our company to edit at later date. Images must be licenced for use.

The text to be included is:

Medical or GP clinic patients

Medical

1 page

• WORDPRESS and use the attached jpg as a design guide.
• Must be able to allow me to insert link to "slot lantern" in the top LEFT CORNER. a button or similar. The slot lantern designers will help us with this, but it must have the space

```html
<!DOCTYPE html>
<html lang="en">
<head>
<meta charset="utf-8">
<title>Harbourline GP</title>
<link href="https://fonts.googleapis.com/css2?family=Open+Sans:wght@400;600;700&display=swap" rel="stylesheet">
<style>
:root{
  --navy:#2e3a8c;
  --green:#5a9a2c;
  --green-btn:#78b12d;
  --ink:#2b2b2b;
  --sky:#1e9be8;
  --sky-pale:#c4e9f8;
  --white:#ffffff;
}
*{margin:0;padding:0;box-sizing:border-box}
html,body{width:1200px;height:2242px;overflow:hidden}
body{position:relative;font-family:"Open Sans",Arial,sans-serif;color:var(--ink);
  background:linear-gradient(180deg,#fff 0,#fff 1700px,#dff3fb 1850px,var(--sky-pale) 2222px)}
.top-rule{position:absolute;left:0;top:0;width:1200px;height:12px;background:var(--navy)}
.booking-btn{position:absolute;left:87px;top:49px;width:190px;height:45px;border-radius:23px;
  background:var(--green-btn);color:#fff;font-weight:700;font-size:17px;display:flex;align-items:center;padding-left:18px;gap:10px}
.booking-btn .dot{width:20px;height:20px;border-radius:50%;background:#fff}
.brand{position:absolute;left:480px;top:60px;width:240px;display:flex;align-items:center;justify-content:center;gap:10px;
  font-weight:600;font-size:24px;color:var(--navy)}
.brand .mark{width:20px;height:20px;background:var(--navy)}
.contact{position:absolute;right:87px;top:48px;text-align:right;font-size:14px;font-weight:600;line-height:27px}
.contact svg{vertical-align:-2px;margin-right:8px}
.hero{position:absolute;left:0;top:135px;width:1200px;height:545px;
  background:linear-gradient(90deg,#86aecd 0%,#b7d2e6 30%,#d9eaf6 50%,#6fc2f2 65%,#2ba6ee 80%,#56b9f1 100%)}
.hero-rule{position:absolute;left:0;top:677px;width:1200px;height:8px;background:var(--navy)}
.hero-box{position:absolute;left:87px;width:572px;color:#fff;text-align:center}
.hero-box.ask{top:223px;height:142px;background:rgba(46,58,140,.88);padding-top:34px;font-size:22px;line-height:34px}
.hero-box.ask b{font-size:27px}
.hero-box.ask .line2{font-size:25px;font-weight:600}
.hero-box.welcome{top:384px;height:220px;background:rgba(90,154,44,.88);padding-top:38px;font-size:18px;line-height:26px;font-weight:600}
.hero-box.welcome .big{font-size:25px;font-weight:700;line-height:40px}
.feature-img{position:absolute;left:87px;width:468px;height:300px;border-bottom:9px solid var(--green)}
.img-stethoscope{top:753px;background:linear-gradient(135deg,#dfe6ee,#6f9fcf 55%,#2d5d9a)}
.img-lab{top:1115px;background:linear-gradient(135deg,#1f6f8f,#8ccde0 50%,#2b8cb0)}
.img-physio{top:1478px;background:linear-gradient(135deg,#e8c9c0,#b9d3ea 55%,#7fb0d8)}
.conditions{position:absolute;left:599px;top:765px;width:495px}
.conditions h2{font-size:20px;font-weight:700;padding-bottom:8px;border-bottom:1px solid #555;width:260px;margin-bottom:14px;white-space:nowrap}
.conditions ul{list-style:none;font-size:13.2px;line-height:25px;margin-left:-4px}
.conditions li{padding-left:16px;position:relative}
.conditions li::before{content:"";position:absolute;left:0;top:9px;width:8px;height:8px;border-radius:50%;background:var(--green)}
.service{position:absolute;left:611px;width:320px;font-size:20px;line-height:31px;font-weight:600}
.service h3{font-size:19px;font-weight:700;margin-bottom:10px}
.service.diag{top:1182px}
.service.physio{top:1510px}
.emergency{position:absolute;left:0;top:1898px;width:1200px;text-align:center;font-weight:600;font-size:20px;line-height:29px}
.emergency .urgent{font-size:28px;font-weight:700;margin-top:12px;line-height:36px}
.emergency .call{font-size:20px;font-weight:700}
.social{position:absolute;left:523px;top:2130px;display:flex;gap:10px}
.social .square{width:59px;height:54px;background:#1f5fa8}
.bottom-rule{position:absolute;left:0;top:2223px;width:1200px;height:19px;background:var(--green)}
</style>
</head>
<body>
<div class="top-rule"></div>

<header>
  <a class="booking-btn"><span class="dot"></span>Slot Lantern</a>
  <div class="brand"><span class="mark"></span>Harbourline GP</div>
  <div class="contact">
    <div><svg width="12" height="12" viewBox="0 0 24 24"><path fill="#5a9a2c" d="M6.6 10.8a15 15 0 0 0 6.6 6.6l2.2-2.2c.3-.3.7-.4 1-.2 1.1.4 2.3.6 3.6.6.6 0 1 .4 1 1V20c0 .6-.4 1-1 1A17 17 0 0 1 3 4c0-.6.4-1 1-1h3.5c.6 0 1 .4 1 1 0 1.3.2 2.5.6 3.6.1.3 0 .7-.2 1z"/></svg>6310 5720</div>
    <div><svg width="13" height="10" viewBox="0 0 26 20"><rect width="26" height="20" rx="2" fill="#5a9a2c"/><path d="M1 2l12 9 12-9" stroke="#fff" stroke-width="2" fill="none"/></svg>reception@harbourlinegp.com.au</div>
  </div>
</header>

<section class="hero" role="img" aria-label="Doctor holding a stethoscope beside a panel of blue medical hexagon icons"></section>
<div class="hero-rule"></div>
<div class="hero-box ask">UNABLE TO GET A <b>DOCTOR'S APPOINTMENT?</b><div class="line2">WE ARE HAPPY TO HELP</div></div>
<div class="hero-box welcome">
  LOCATED IN EASTVALE, WE TAKE APPOINTMENTS<br>AND WALK IN PATIENTS.
  <div class="big">NEW PATIENTS WELCOME.</div>
  ALL BASIC AND URGENT MEDICAL CARE<br>(NON LIFE THREATENING).
</div>

<div class="feature-img img-stethoscope" role="img" aria-label="Stethoscope resting on a medical chart"></div>
<div class="conditions">
  <h2>GENERAL MEDICAL CONDITIONS</h2>
  <ul>
    <li>chronic conditions such as diabetes, asthma, copd, emphysema, and chronic heart disease and chronic kidney disease.</li>
    <li>wound management and dermatology individualised health care planning</li>
    <li>health promotion activities (clinics, cholesterol and blood sugar checking, smoking advice)</li>
    <li>work related injury management</li>
    <li>immunisations</li>
    <li>mental health</li>
    <li>motor vehicle accident assessment</li>
  </ul>
</div>

<div class="feature-img img-lab" role="img" aria-label="Laboratory scientist pipetting samples into glassware"></div>
<div class="service diag">
  <h3>AT HARBOURLINE GP,</h3>
  We are able to undertake<br>a range of<br>diagnostic services<br>including pathology.
</div>

<div class="feature-img img-physio" role="img" aria-label="Physiotherapist assisting an elderly patient with arm exercises"></div>
<div class="service physio">
  <h3>AT HARBOURLINE GP,</h3>
  we have a physiotherapy<br>service that can assist<br>in managing your<br>musculo-skeletal conditions,<br>sporting injuries and<br>post injury rehabilitation.
</div>

<section class="emergency">
  IF YOU ARE EXPERIENCING ANY CHEST PAIN,<br>
  DIFFICULTY WITH BREATHING OR ANY ACUTE SYMPTOMS ASSOCIATED WITH THE<br>
  HEART, LUNGS, OR BRAIN,
  <div class="urgent">PLEASE GO TO YOUR NEAREST HOSPITAL</div>
  <div class="call">OR CALL THE COASTLINE AMBULANCE ON 000 IMMEDIATELY.</div>
  DO NOT WAIT IN THE WAITING ROOM.
</section>

<div class="social">
  <div class="square"></div>
  <svg width="82" height="54" viewBox="0 0 82 54"><rect width="82" height="54" fill="#2a56a8"/><path d="M2 3l39 28 39-28M2 52l28-24M80 52L52 28" stroke="#fff" stroke-width="4" fill="none"/></svg>
</div>

<div class="bottom-rule"></div>
</body>
</html>
```